Website for Brivex Partners

We need to create a website for our company. Attached is the site map of the website and data input needed. Our theme colour is RED and our Logo is attached

We need a very attractive design where graphics are largely used like flash.

The main idea of the website is to show Telecommunications Suppliers World Wide that we could assist them in getting more business in Africa and Middle East through our local presence in this region.
Updates

Target Market(s)

Telecommunication Suppliers and Clients

Industry/Entity Type

Business

Font styles to use
Serif
Sans Serif

Colors
ec2027

Requirements
Must have
• Graphics that shows Telecommunications Suppliers World Wide that we could assist them in getting more business in Africa and Middle East through our local presence in this region.

The website should be easy to edit for future changes by us.
Nice to have
• New ideas

```html
<!DOCTYPE html>
<html lang="en">
<head>
<meta charset="utf-8">
<title>Brivex Partners</title>
<link href="https://fonts.googleapis.com/css2?family=Arimo:wght@400;700&display=swap" rel="stylesheet">
<style>
:root{
  --red:#ec2027;
  --bg:#1f1f1f;
  --header:#1c1c1c;
  --panel:#2f2f2f;
  --panel-dark:#1e1e1e;
  --card:#1b1b1b;
  --text:#ffffff;
  --muted:#8d8d8d;
  --soft:#bdbdbd;
  --line:#3a3a3a;
}
*{margin:0;padding:0;box-sizing:border-box}
html,body{width:1200px;height:1000px;overflow:hidden;background:var(--bg);font-family:"Arimo",Arial,sans-serif;color:var(--text)}
.page{position:relative;width:1200px;height:1000px}
.abs{position:absolute}

/* header */
.site-header{left:0;top:0;width:1200px;height:57px;background:var(--header);border-bottom:1px solid #2c2c2c}
.brand{left:140px;top:12px;display:flex;align-items:center}
.brand-square{width:34px;height:30px;background:var(--text);margin-right:12px}
.brand-text{border-left:1px solid var(--text);padding-left:8px}
.brand-name{font-size:25px;font-weight:700;line-height:24px;letter-spacing:.5px;text-transform:uppercase}
.brand-tagline{font-size:7.5px;letter-spacing:3.2px;line-height:9px;text-transform:uppercase}
.main-nav{left:680px;top:0;display:flex;height:57px}
.main-nav a{display:block;color:var(--text);text-decoration:none;font-size:10px;font-weight:700;line-height:60px;padding:0 17px}
.main-nav a.active{background:var(--red);padding:0 22px;width:71px}

/* hero */
.hero{left:0;top:57px;width:1200px;height:334px;background:radial-gradient(ellipse 70% 60% at 40% 95%,#8a8a8a 0%,#4d4d4d 35%,#1b1b1b 70%),#111}
.slider-dots{left:160px;top:363px;display:flex;gap:6px}
.slider-dots span{width:8px;height:8px;border-radius:50%;background:#fff}
.slider-dots span.on{background:var(--red)}
.feature{left:785px;width:301px;height:89px;background:var(--card);padding:21px 0 0 24px}
.feature h3{font-size:25px;font-weight:400;color:#cfcfcf;line-height:28px}
.feature p{font-size:11px;color:#8a8a8a;text-transform:uppercase;margin-top:2px}
.feature.first h3{color:var(--text)}
.feature.first p{color:var(--red)}
.feature svg{position:absolute;right:51px;top:26px}

/* content */
.content{left:140px;top:379px;width:946px;height:520px;background:linear-gradient(#333 0%,#2b2b2b 60%,#232323 100%)}
.intro{left:160px;top:408px;width:600px}
.intro h1{font-size:16px;font-weight:400;line-height:19px}
.intro h2{font-size:10px;font-weight:700;margin-top:24px;color:#e8e8e8}
.intro p{font-size:9px;line-height:16px;color:var(--muted);margin-top:22px;width:560px}
.link-red{color:var(--red);text-decoration:underline}

.who{left:160px;top:621px;width:300px}
.section-title{font-size:15px;font-weight:400;color:#e6e6e6}
.who .sub{font-size:12px;color:#e6e6e6;margin-top:1px}
.photo{left:160px;top:677px;width:268px;height:124px;background:linear-gradient(100deg,#2a2a2a 0%,#7a7a7a 45%,#cfcfcf 70%,#5a5a5a 100%)}
.who-text{left:160px;top:817px;width:290px;font-size:9px;line-height:16.5px;color:#7d7d7d}
.divider{left:493px;top:627px;width:1px;height:257px;background:#4a4a4a}
.portfolio{left:532px;top:621px}
.portfolio ul{list-style:none;margin-top:37px}
.portfolio li{font-size:9px;color:#b9b9b9;height:21px;padding-left:23px;position:relative}
.portfolio li::before{content:"»";position:absolute;left:0;top:-1px;color:#777}
.portfolio .more{display:block;font-size:8px;color:#aaa;text-decoration:underline;margin-top:23px;font-weight:700}

/* capabilities */
.capabilities{left:786px;top:396px;width:285px;height:500px;background:linear-gradient(#1e1e1e,#252525 80%,#2b2b2b)}
.capabilities .section-title{position:absolute;left:24px;top:25px}
.cap{position:absolute;left:24px;width:240px}
.cap svg{position:absolute;left:0;top:0}
.cap h4{margin-left:54px;font-size:9px;font-weight:700;text-decoration:underline;color:var(--text)}
.cap.vision h4{color:var(--red)}
.cap p{margin-left:54px;font-size:9px;line-height:16px;color:var(--muted);margin-top:3px}
.cta{left:810px;top:677px;width:240px;height:143px;background:var(--red);padding:34px 0 0 31px}
.cta h5{font-size:15px;font-weight:700;line-height:17px}
.cta p{font-size:11px;font-weight:700}
.cta a{display:block;width:113px;height:35px;margin:18px 0 0 28px;background:#1a1a1a;border-radius:3px;color:#fff;font-size:10px;font-weight:700;text-align:center;line-height:35px;text-decoration:none}

/* footer */
.footer-line{left:140px;top:930px;width:946px;height:1px;background:#353535}
.footer-brand{left:140px;top:958px;display:flex;align-items:center;gap:10px;height:30px}
.footer-brand .name{font-size:13px;font-weight:700;color:#6f6f6f;text-transform:uppercase;padding-right:10px;border-right:1px solid #555;line-height:30px}
.social{display:flex;gap:7px}
.social span{width:19px;height:19px;border-radius:50%;background:#6f6f6f}
.copyright{right:117px;top:964px;font-size:7.5px;color:#8a8a8a;text-transform:uppercase}
</style>
</head>
<body>
<div class="page">
  <header class="site-header abs">
    <div class="brand abs">
      <div class="brand-square"></div>
      <div class="brand-text">
        <div class="brand-name">Brivex Partners</div>
        <div class="brand-tagline">Your challenge is our business</div>
      </div>
    </div>
    <nav class="main-nav abs">
      <a class="active" href="#">HOME</a>
      <a href="#">COMPANY</a>
      <a href="#">PORTFOLIO</a>
      <a href="#">FOOTPRINT</a>
      <a href="#">CONTACT US</a>
    </nav>
  </header>

  <section class="hero abs" role="img" aria-label="Night view of the globe from space with glowing network arcs linking cities"></section>
  <div class="slider-dots abs"><span class="on"></span><span></span><span></span><span></span></div>

  <div class="feature first abs" style="top:87px">
    <h3>Easy Access</h3><p>Just 3 step to begin</p>
    <svg width="38" height="38" viewBox="0 0 38 38"><circle cx="19" cy="19" r="18" fill="none" stroke="#ec2027" stroke-width="1.2"/><path d="M16 12l7 7-7 7" fill="none" stroke="#ec2027" stroke-width="1.2"/></svg>
  </div>
  <div class="feature abs" style="top:181px">
    <h3>Worldwide</h3><p>Call anytime anywhere</p>
    <svg width="38" height="38" viewBox="0 0 38 38"><circle cx="19" cy="19" r="18" fill="none" stroke="#777" stroke-width="1.2"/><path d="M16 12l7 7-7 7" fill="none" stroke="#777" stroke-width="1.2"/></svg>
  </div>
  <div class="feature abs" style="top:276px">
    <h3>24/7 Support</h3><p>Unlimited support services</p>
    <svg width="38" height="38" viewBox="0 0 38 38"><circle cx="19" cy="19" r="18" fill="none" stroke="#777" stroke-width="1.2"/><path d="M16 12l7 7-7 7" fill="none" stroke="#777" stroke-width="1.2"/></svg>
  </div>

  <main class="content abs"></main>
  <div class="intro abs">
    <h1>Our company is a leading international provider of the<br>BEST TELECOMMUNICATIONS SERVICES.</h1>
    <h2>Your Challenge is Our Business</h2>
    <p>Brivex Partners is a leading telecommunication Solution Provider; The company provides state of the art technologies and turnkey solutions to its clients that fully support their business needs from planning right through full operation, our methodology is to work hand in hand with our clients in all sectors and support their business needs from inception to completion. &nbsp;<a class="link-red" href="#">read more</a></p>
  </div>

  <div class="who abs">
    <div class="section-title">who we are</div>
    <div class="sub">the best teleconnection for your better communication!</div>
  </div>
  <div class="photo abs" role="img" aria-label="Server rack beside a glowing globe"></div>
  <p class="who-text abs">Brivex Partners is a leading telecommunication Solution Provider; the company provides state of the art technologies and turnkey solutions to its clients that fully support their business needs from planning right through full operation [......]</p>
  <div class="divider abs"></div>
  <div class="portfolio abs">
    <div class="section-title">our portfolio</div>
    <ul>
      <li>Access Network Solutions</li>
      <li>Transmission Network Solutions</li>
      <li>Core Network Solutions</li>
      <li>Value Added Services</li>
      <li>Managed Services</li>
      <li>Business Consultancy</li>
    </ul>
    <a class="more" href="#">READ MORE</a>
  </div>

  <aside class="capabilities abs">
    <div class="section-title">our capabilities</div>
    <div class="cap vision" style="top:64px">
      <svg width="22" height="32" viewBox="0 0 22 32"><path d="M11 2a9 9 0 0 0-5 16.5V23h10v-4.5A9 9 0 0 0 11 2z" fill="none" stroke="#ec2027" stroke-width="1.5"/><path d="M7 26h8M8 29h6M11 10v12M8 13l3 3 3-3" fill="none" stroke="#ec2027" stroke-width="1.3"/></svg>
      <h4>Our Vision</h4>
      <p>Becoming the service partner of choice for Communication &amp; Information technology services.</p>
    </div>
    <div class="cap" style="top:145px">
      <svg width="22" height="28" viewBox="0 0 22 28"><path d="M1 12A10 10 0 0 1 21 12z" fill="#6e6e6e"/><path d="M11 12v11a2.5 2.5 0 0 1-5 0" fill="none" stroke="#6e6e6e" stroke-width="1.6"/></svg>
      <h4>Our Mission</h4>
      <p>Leveraging telecommunications edge by providing world class support and services that empower people to connect and businesses to grow.</p>
    </div>
  </aside>
  <div class="cta abs">
    <h5>TELECOMMUNICATION</h5>
    <p>FOR MORE DETAILS</p>
    <a href="#">CLICK HERE</a>
  </div>

  <div class="footer-line abs"></div>
  <footer class="footer-brand abs">
    <div class="name">Brivex</div>
    <div class="social"><span></span><span></span><span></span><span></span><span></span><span></span></div>
  </footer>
  <div class="copyright abs">© 2014 Company Name &nbsp;| &nbsp;Privacy Policy</div>
</div>
</body>
</html>
```